Modernize an Old Theme (One Page Simple Design)

So we have a older theme in our Shopping Cart software that people love to use. In an effort to modernize the theme and make it responsive, we are looking to have it re designed. This project should be very easy to complete and here are the details:

1. We only need the one, main page, actually designed and just the PSD created. We will have someone else cut it up and make it responsive.

2. The design should be modernized and include elements such as a slide show place holder and and updated product tiling look.

3. The current theme can be viewed here: http://demo.brivlo.example//index.php?theme=classic_black - We want it to look like the current theme with the 3 columns. The classic look just modernized.

4. The social buttons can be updated and placed in the footer if possible. We would like to use a chirpnet widget and pagebook like widget like on this newer theme here http://demo.brivlo.example/index.php?theme=tallmart_responsive

5. Keep in mind that the main color (black) in #3 theme link being redesigned, needs to easily be changeable via css when we create the HTML so avoid textures or backgrounds that would prevent this from happening.

Important Note: We want it to look like the current theme example linked in the description above with the 3 columns. The classic black theme. We just want to make it more modern looking

Requirements
Must have
• See description.
Nice to have
• See description.
Should not have
• See description.

```html
<!DOCTYPE html>
<html lang="en">
<head>
<meta charset="utf-8">
<title>Brivlo Store</title>
<link href="https://fonts.googleapis.com/css2?family=Open+Sans:wght@400;600;700&display=swap" rel="stylesheet">
<style>
:root{
  --accent:#f26f21;
  --ink:#333;
  --muted:#777;
  --line:#e2e2e2;
  --dark:#2b2b2b;
  --footer:#f1f1f1;
  --white:#fff;
}
*{box-sizing:border-box;margin:0;padding:0}
html,body{width:1200px;height:2660px;overflow:hidden}
body{font-family:"Open Sans",Arial,sans-serif;color:var(--ink);background:var(--white);position:relative;font-size:12px}
.abs{position:absolute}
a{color:inherit;text-decoration:none}
ul{list-style:none}

.topbar{left:0;top:0;width:1200px;height:28px;background:var(--dark);color:#ccc;font-size:11px;display:flex;align-items:center;justify-content:space-between;padding:0 100px}
.topbar span{margin-right:18px}
.topbar .dot{display:inline-block;width:7px;height:7px;border-radius:50%;background:var(--accent);margin-right:5px}

.header{left:0;top:28px;width:1200px;height:92px}
.logo{left:100px;top:26px;font-size:30px;font-weight:700;color:var(--accent);display:flex;align-items:center;gap:8px}
.logo i{display:block;width:18px;height:18px;border-radius:50%;background:var(--accent)}
.search{left:460px;top:32px;width:300px;height:30px;border:1px solid #ccc;display:flex}
.search span{flex:1;padding:6px 10px;color:#aaa;font-size:11px}
.search b{width:34px;background:#eee;border-left:1px solid #ccc}
.cart{left:935px;top:30px;display:flex;gap:10px;align-items:center}
.cart .title{font-weight:600;font-size:12px}
.cart .sub{font-size:11px;color:var(--muted)}

.nav{left:0;top:120px;width:1200px;height:45px;border-top:1px solid var(--line);border-bottom:2px solid var(--accent);display:flex;justify-content:center;gap:56px;align-items:center;font-size:13px;font-weight:600}
.nav .active{color:var(--accent)}

.hero{left:0;top:167px;width:1200px;height:360px;background:linear-gradient(90deg,#d9d9d9,#f5f5f5 45%,#e4e4e4)}
.hero h1{position:absolute;left:100px;top:80px;font-size:36px;color:#555;font-weight:700}
.hero p{position:absolute;left:100px;top:136px;width:330px;font-size:12px;color:#666;line-height:1.6}
.hero .btn{position:absolute;left:100px;top:204px;border:2px solid var(--accent);color:var(--accent);font-weight:700;font-size:12px;padding:7px 18px}
.hero .devices{position:absolute;left:560px;top:40px;width:520px;height:280px;background:linear-gradient(135deg,#9aa3ad,#3a4550);border-radius:6px}
.hero .arrow{position:absolute;top:155px;width:24px;height:40px;background:rgba(0,0,0,.15)}
.hero .dots{position:absolute;left:560px;top:334px;display:flex;gap:8px}
.hero .dots i{width:9px;height:9px;border-radius:50%;background:#bbb}
.hero .dots i:first-child{background:var(--accent)}

.side-head{background:var(--accent);color:#fff;font-weight:700;font-size:15px;padding:9px 12px}
.side-box{border:1px solid var(--line);background:var(--white)}
.cats li{padding:7px 14px;font-size:11.5px;border-bottom:1px solid #f0f0f0;display:flex;align-items:center;gap:8px}
.cats li:before{content:"";width:6px;height:6px;border-radius:50%;border:1px solid var(--accent);flex:none}
.select{margin:10px 12px;border:1px solid #ccc;padding:5px 8px;font-size:11px;color:var(--muted);white-space:nowrap}
.sale{display:flex;gap:10px;padding:12px}
.sale .thumb{width:52px;height:52px;background:linear-gradient(#777,#333);flex:none}
.sale .n{font-size:11px;line-height:1.4}
.price{color:var(--accent);font-weight:700;font-size:13px}

.section-title{font-size:22px;font-weight:600;color:#444}
.card{position:absolute;width:210px}
.card .img{height:160px;border:1px solid var(--line);display:flex;align-items:center;justify-content:center}
.card .img div{width:115px;height:115px;border-radius:4px}
.card .name{margin-top:16px;font-size:12px;line-height:1.5;height:54px}
.card .price{margin-top:14px;display:block}
.stars{color:var(--accent);font-size:11px;margin-top:4px;letter-spacing:1px}
.card .btns{display:flex;gap:6px;margin-top:14px}
.b-add{background:var(--accent);color:#fff;font-size:10px;font-weight:700;padding:6px 8px;white-space:nowrap}
.b-more{border:1px solid #ccc;color:#555;font-size:10px;font-weight:700;padding:5px 8px;white-space:nowrap}
.viewmore{left:390px;top:1500px;font-size:11px;font-weight:700;color:var(--accent)}

.rule{height:1px;background:var(--line)}
.best{position:absolute;width:150px}
.best .img{height:110px;border-radius:2px}
.best .name{font-size:11px;margin-top:10px;line-height:1.4}
.c-arrow{position:absolute;width:22px;height:34px;background:var(--dark);color:#fff;font-size:16px;display:flex;align-items:center;justify-content:center}

.widget-title{font-size:20px;font-weight:600}
.fb{border:1px solid var(--line)}
.fb .cover{height:150px;background:linear-gradient(90deg,#f7a96c,#fde3cf)}
.fb .row{display:flex;align-items:center;gap:10px;padding:10px}
.fb .ava{width:42px;height:42px;background:var(--accent)}
.fb .like{border:1px solid #ccc;font-size:10px;padding:3px 8px;background:#f6f6f6}
.fb .faces{display:flex;gap:6px;padding:0 10px 12px}
.fb .faces i{width:34px;height:34px;background:#c9c9c9}
.tw{border:1px solid var(--line)}
.tweet{display:flex;gap:12px;padding:14px;border-bottom:1px solid #eee}
.tweet .ava{width:48px;height:48px;background:var(--accent);border-radius:4px;flex:none}
.tweet .who{font-size:12px;font-weight:700}
.tweet .who span{font-weight:400;color:var(--accent);margin-left:6px}
.tweet p{font-size:11px;color:var(--muted);margin-top:4px;line-height:1.5}
.tweet .acts{display:flex;gap:30px;margin-top:8px}
.tweet .acts i{width:12px;height:10px;background:#ccc}

.footer{left:0;top:2280px;width:1200px;height:340px;background:var(--footer);border-top:3px solid var(--accent)}
.fcol{position:absolute;top:60px}
.fcol h4{font-size:14px;font-weight:700;margin-bottom:14px}
.fcol li{font-size:11px;color:var(--muted);margin-bottom:8px}
.news-in{display:flex;margin-top:14px}
.news-in span{width:220px;border:1px solid #ccc;background:#fff;padding:7px;font-size:11px;color:#aaa}
.news-in b{background:var(--accent);color:#fff;font-size:11px;padding:8px 14px}
.social{display:flex;gap:8px;margin-top:10px}
.social i{width:26px;height:26px;border-radius:50%;background:var(--accent)}
.copy{left:0;top:2620px;width:1200px;height:40px;background:var(--dark);color:#aaa;font-size:11px;display:flex;align-items:center;justify-content:center}
</style>
</head>
<body>

<div class="abs topbar">
  <div><span><i class="dot"></i>1-800-555-0142</span><span><i class="dot"></i>hello@brivlo.example</span></div>
  <div><span>Currency</span><span>My Account</span><span>Login | Create Account</span></div>
</div>

<div class="abs header">
  <div class="abs logo"><i></i>Brivlo</div>
  <div class="abs search"><span>Search</span><b></b></div>
  <div class="abs cart">
    <svg width="26" height="24" viewBox="0 0 26 24"><path d="M1 2h4l3 13h13l3-9H7" fill="none" stroke="#f26f21" stroke-width="2"/><circle cx="10" cy="20" r="2" fill="#f26f21"/><circle cx="19" cy="20" r="2" fill="#f26f21"/></svg>
    <div><div class="title">My Cart</div><div class="sub">0 item(s) - $0.00</div></div>
  </div>
</div>

<nav class="abs nav">
  <a class="active">Home</a><a>Gift Registry</a><a>Gift Certificates</a><a>Privacy Policy</a><a>About Us</a><a>Contact Us</a>
</nav>

<section class="abs hero">
  <div class="arrow" style="left:0"></div>
  <div class="arrow" style="right:0"></div>
  <h1>Brivlo</h1>
  <p>A clean place for our newest arrivals and weekly deals, picked with care and ready to ship today.</p>
  <a class="btn">SHOP NOW</a>
  <div class="devices" role="img" aria-label="Laptop, tablets and phones arranged together"></div>
  <div class="dots"><i></i><i></i><i></i></div>
</section>

<aside class="abs" style="left:100px;top:640px;width:200px">
  <div class="side-box">
    <div class="side-head">Categories</div>
    <ul class="cats">
      <li>New Products</li><li>Specials</li><li>Featured</li><li>Bestsellers</li><li>Books &amp; Magazines</li><li>Movies, Music &amp; Games</li><li>Digital Downloads</li><li>Computers &amp; Office</li><li>Electronics</li><li>Sports &amp; Outdoors</li>
    </ul>
  </div>
  <div class="side-box" style="margin-top:14px">
    <div class="side-head">Manufacturers</div>
    <div class="select">Select a Manufacturer ▾</div>
  </div>
  <div class="side-box" style="margin-top:14px">
    <div class="side-head">Sales Items</div>
    <div class="sale"><div class="thumb" role="img" aria-label="Laptop product photo"></div><div><div class="n">Arvel Strata 15 Laptop Notebook</div><div class="price">$329.99</div></div></div>
    <div class="sale"><div class="thumb" role="img" aria-label="Phone product photo"></div><div><div class="n">Simple 4 Smart Phone Unlocked</div><div class="price">$19.50</div></div></div>
  </div>
</aside>

<h2 class="abs section-title" style="left:390px;top:640px">Featured Products</h2>

<div class="card" style="left:390px;top:700px"><div class="img"><div style="background:linear-gradient(#6b4f8a,#222)" role="img" aria-label="Laser sport crystals product"></div></div><div class="name">Laser Sport Crystals With Light Up Base...</div><span class="price">$11.49</span><div class="stars">★★★★★</div><div class="btns"><span class="b-add">ADD TO CART</span><span class="b-more">MORE DETAILS</span></div></div>
<div class="card" style="left:635px;top:700px"><div class="img"><div style="background:linear-gradient(#d8d8d8,#8a8a8a)" role="img" aria-label="Desktop gaming PC tower"></div></div><div class="name">Custom Nexcore Z-Series Gaming PC Thru Build Yo...</div><span class="price">$1999.00</span><div class="stars">★★★★★</div><div class="btns"><span class="b-add">ADD TO CART</span><span class="b-more">MORE DETAILS</span></div></div>
<div class="card" style="left:880px;top:700px"><div class="img"><div style="background:linear-gradient(#555,#111)" role="img" aria-label="Digital SLR camera"></div></div><div class="name">Optiva DX12 12.3 MP Digital SLR Camera with 18-55mm...</div><span class="price">Add to cart to see price</span><div class="stars">★★★★★</div><div class="btns"><span class="b-add">ADD TO CART</span><span class="b-more">MORE DETAILS</span></div></div>

<div class="card" style="left:390px;top:1120px"><div class="img"><div style="background:linear-gradient(#3a6f9a,#111)" role="img" aria-label="Flat screen LCD television"></div></div><div class="name">Vistar VQ32 32-Inch 1080p LCD HDTV</div><span class="price">$389.99</span><div class="stars">★★★★★</div><div class="btns"><span class="b-add">ADD TO CART</span><span class="b-more">MORE DETAILS</span></div></div>
<div class="card" style="left:635px;top:1120px"><div class="img"><div style="background:linear-gradient(#7a3a2a,#1a1a1a)" role="img" aria-label="Television showing sports"></div></div><div class="name">Solmara SL58 58-Inch 1080p LED HDTV</div><span class="price">$2399.99</span><div class="stars">★★★★★</div><div class="btns"><span class="b-add">ADD TO CART</span><span class="b-more">MORE DETAILS</span></div></div>
<div class="card" style="left:880px;top:1120px"><div class="img"><div style="background:linear-gradient(#5a3f8a,#222)" role="img" aria-label="Laptop computer open"></div></div><div class="name">Arvel Strata 15 15.6-Inch Laptop Black...</div><span class="price">$394.99</span><div class="stars">★★★★★</div><div class="btns"><span class="b-add">ADD TO CART</span><span class="b-more">MORE DETAILS</span></div></div>

<a class="abs viewmore">VIEW MORE PRODUCTS →</a>

<div class="abs rule" style="left:100px;top:1570px;width:1000px"></div>
<h2 class="abs section-title" style="left:0;top:1600px;width:1200px;text-align:center">Bestsellers</h2>
<div class="c-arrow" style="left:74px;top:1700px">‹</div>
<div class="c-arrow" style="left:1104px;top:1700px">›</div>
<div class="best" style="left:100px;top:1665px"><div class="img" style="background:linear-gradient(#3b5a7a,#111)" role="img" aria-label="Game case cover"></div><div class="name">Zenbox Frontline Ops Limited Edition Console</div></div>
<div class="best" style="left:270px;top:1665px"><div class="img" style="background:linear-gradient(#c7a23a,#4a2a10)" role="img" aria-label="Game case cover"></div><div class="name">Pocket Champions HD Game (Download)</div></div>
<div class="best" style="left:440px;top:1665px"><div class="img" style="background:linear-gradient(#7a2a1a,#111)" role="img" aria-label="Game case cover"></div><div class="name">Warrior Brothers and the Free Frontier</div></div>
<div class="best" style="left:610px;top:1665px"><div class="img" style="background:linear-gradient(#2a3a4a,#0a0a0a)" role="img" aria-label="Game case cover"></div><div class="name">Star Quest Galactic Saga Large Bonus Pack Bundle</div></div>
<div class="best" style="left:780px;top:1665px"><div class="img" style="background:linear-gradient(#4a6a3a,#111)" role="img" aria-label="Game case cover"></div><div class="name">Star Ride Motion Racing Edition (Disc)</div></div>
<div class="best" style="left:950px;top:1665px"><div class="img" style="background:linear-gradient(#444,#000)" role="img" aria-label="Game console with controller"></div><div class="name">Zenbox Game Console 250GB Black Bundle</div></div>

<div class="abs rule" style="left:100px;top:1890px;width:1000px"></div>

<h3 class="abs widget-title" style="left:100px;top:1925px">Join us on pagebook</h3>
<div class="abs fb" style="left:100px;top:1970px;width:425px">
  <div class="cover" role="img" aria-label="Store page cover photo"></div>
  <div class="row"><div class="ava"></div><div><div style="font-weight:700;font-size:12px">Brivlo Store</div><div style="font-size:10px;color:#888">4,120 likes</div></div><span class="like" style="margin-left:auto">Like Page</span></div>
  <div style="font-size:10px;color:#888;padding:0 10px 8px">Be the first of your friends to like this</div>
  <div class="faces"><i></i><i></i><i></i><i></i><i></i><i></i><i></i><i></i><i></i><i></i></div>
</div>

<h3 class="abs widget-title" style="left:625px;top:1925px">Tweets</h3>
<div class="abs tw" style="left:625px;top:1970px;width:475px">
  <div class="tweet"><div class="ava"></div><div><div class="who">Keystone Web Kit<span>@keystonewebkit</span></div><p>Thank you to all who have visited our chirpnet page this week!</p><div class="acts"><i></i><i></i><i></i></div></div></div>
  <div class="tweet"><div class="ava"></div><div><div class="who">Keystone Web Kit<span>@keystonewebkit</span></div><p>New release notes are now live, take a look and share ideas with us.</p><div class="acts"><i></i><i></i><i></i></div></div></div>
  <div class="tweet" style="border-bottom:0"><div class="ava"></div><div><div class="who">Keystone Web Kit<span>@keystonewebkit</span></div><p>Thanks for all the support, more updates coming soon.</p><div class="acts"><i></i><i></i><i></i></div></div></div>
</div>

<footer class="abs footer">
  <div class="fcol" style="left:100px"><h4>Information</h4><ul><li>Gift Registry</li><li>Gift Certificates</li><li>Privacy Policy</li><li>About Us</li><li>Contact Us</li><li>Site Map</li></ul></div>
  <div class="fcol" style="left:330px"><h4>Help &amp; support</h4><ul><li>Recommended Reading</li><li>Submission Form</li><li>Contact Us</li><li>Frequently Asked Questions</li><li>How to Order</li></ul></div>
  <div class="fcol" style="left:560px"><h4>My Account</h4><ul><li>Delivery Information</li><li>My Account</li><li>Order Tracking</li><li>Reorder Service</li><li>Shipping, Returns &amp; Info</li></ul></div>
  <div class="fcol" style="left:800px"><h4>Newsletter Signup</h4><div style="font-size:11px;color:#777">Register your email address to get information about us</div><div class="news-in"><span>Email address</span><b>SIGN UP</b></div><h4 style="margin-top:22px;margin-bottom:0">Stay Connected</h4><div class="social"><i></i><i></i><i></i><i></i><i></i><i></i><i></i><i></i></div></div>
</footer>
<div class="abs copy">Copyright © 2015 Brivlo. All Rights Reserved &nbsp;|&nbsp; Privacy Policy &nbsp;|&nbsp; Terms of Use &nbsp;|&nbsp; Feedback</div>

</body>
</html>
```